Business Card for Yachting Management Company

Need a business card design for a new yachting project management company. Attached is the logo for the company.
Our clients are large yacht owners and captains.
Design must be in the style of the logo. Modern, elegant.

Example of data to show:
Peter Hollis
Project Manager
(+34) 612 738 104
peter@quorvane.net
Quorvane Management - Meridel Tower, Office 22 - KRB - Palma de Mallorca

The data above will have to be changed (by me) for the different people in the company over the next years.

Will be printed using PrintNova (Lustre Card Series). They provide these guidelines for the size:
"the actual size of the card is 1050 x 600 pixels. However, the full bleed size is 1083 x 633 pixels, and the safe printing area is 1008 x 558 pixels."

```html
<!DOCTYPE html>
<html lang="en">
<head>
<meta charset="utf-8">
<title>Quorvane Management – Business Card</title>
<link rel="stylesheet" href="https://fonts.googleapis.com/css2?family=Exo+2:wght@400;600;700&display=swap">
<style>
  :root {
    --backdrop: #2a2a2c;
    --card: #1c1d1f;
    --card-back-dark: #0b0b0c;
    --card-back-light: #3a3a3c;
    --brand-blue: #0a74c8;
    --text-grey: #8d8f93;
    --rule: #45474b;
  }
  * { margin: 0; padding: 0; box-sizing: border-box; }
  html, body {
    width: 1200px;
    height: 1108px;
    overflow: hidden;
    background: var(--backdrop);
    font-family: "Exo 2", sans-serif;
  }
  .canvas {
    position: relative;
    width: 1200px;
    height: 1108px;
    display: flex;
    justify-content: center;
    align-items: center;
    gap: 80px;
  }
  .card {
    width: 340px;
    height: 595px;
    border-radius: 22px;
    position: relative;
    overflow: hidden;
  }
  .card-front {
    background: var(--card);
    display: flex;
    flex-direction: column;
    align-items: center;
    text-align: center;
  }
  .brand-name {
    margin-top: 118px;
    font-size: 58px;
    font-weight: 700;
    color: var(--brand-blue);
    letter-spacing: 1px;
  }
  .person-name {
    margin-top: 150px;
    font-size: 24px;
    font-weight: 600;
    letter-spacing: 2px;
    text-transform: uppercase;
    color: var(--brand-blue);
  }
  .person-role {
    font-size: 15px;
    color: var(--text-grey);
    margin-top: 2px;
  }
  .rule {
    width: 140px;
    height: 1px;
    background: var(--rule);
    margin: 14px 0;
  }
  .contact-line {
    font-size: 16px;
    color: var(--text-grey);
    line-height: 1.45;
    letter-spacing: 0.5px;
  }
  .company-name {
    font-size: 16px;
    font-weight: 700;
    color: var(--brand-blue);
  }
  .address-line {
    font-size: 16px;
    color: var(--text-grey);
    line-height: 1.4;
  }
  .card-back {
    background: linear-gradient(225deg, var(--card-back-light) 0%, #1c1c1e 45%, var(--card-back-dark) 100%);
  }
  .back-pattern {
    position: absolute;
    inset: 0;
    background: linear-gradient(225deg, rgba(120,120,124,0.35) 0%, rgba(40,40,42,0.2) 50%, rgba(0,0,0,0.3) 100%);
  }
  .back-brand {
    position: absolute;
    left: 0;
    right: 0;
    top: 452px;
    text-align: center;
    font-size: 30px;
    font-weight: 700;
    color: var(--brand-blue);
    letter-spacing: 0.5px;
  }
</style>
</head>
<body>
  <main class="canvas">
    <section class="card card-front">
      <div class="brand-name">Quorvane</div>
      <h1 class="person-name">Peter Hollis</h1>
      <p class="person-role">Project Manager</p>
      <div class="rule"></div>
      <p class="contact-line">(+34) 612 738 104</p>
      <p class="contact-line">peter@quorvane.net</p>
      <div class="rule"></div>
      <p class="company-name">Quorvane Management</p>
      <p class="address-line">Meridel Tower, Office 22 - KRB</p>
      <p class="address-line">Palma de Mallorca</p>
    </section>
    <section class="card card-back">
      <div class="back-pattern" role="img" aria-label="Repeating tonal brand-name pattern in glossy black and grey"></div>
      <div class="back-brand">Quorvane</div>
    </section>
  </main>
</body>
</html>
```